Lanterns Over Harbor Gate: Notes on Quiet Ambition

I need a book cover. The genre is self-help. would like something that looks original. The book is a barber's story. A barber who earns an M.B.A. I don't mind some type of scissor but I do not want it held to a cosmetology market. Something that speaks to everyone. No stock images. Format 4.25" x 7" This is what book printers call a pocket book.

Requirements
Must have
• Original cover. No stock images.
Nice to have
• I like scissors. Maybe stick men. Creativity
Should not have
• No Stock Images. No Clippers

```html
<!DOCTYPE html>
<html lang="en">
<head>
<meta charset="utf-8">
<title>Lanterns Over Harbor Gate — Cover</title>
<link rel="stylesheet" href="https://fonts.googleapis.com/css2?family=Anton&family=Roboto+Condensed:wght@300;400&display=swap">
<style>
  :root {
    --backdrop: #8b8b8b;
    --paper: #ebebeb;
    --navy: #06324f;
    --navy-deep: #0d1a2a;
    --red: #b01c2a;
    --band-text: #ececec;
    --rule-grey: #a9adb2;
    --figure-top: #8a8479;
    --figure-bottom: #3b3a2c;
  }
  * { box-sizing: border-box; margin: 0; padding: 0; }
  html, body {
    width: 1200px; height: 1200px; overflow: hidden;
    background: var(--backdrop);
  }
  .cover {
    position: absolute; left: 239px; top: 50px;
    width: 722px; height: 1100px;
    background: var(--paper);
    overflow: hidden;
  }
  .title-main, .title-link, .title-accent, .subtitle, .author {
    position: absolute; left: 0; width: 100%;
    text-align: center; white-space: nowrap;
  }
  .title-main {
    top: 178px;
    font-family: "Anton", sans-serif;
    font-size: 150px; line-height: 1;
    color: var(--navy);
  }
  .title-link {
    top: 372px; height: 100px;
    display: flex; align-items: center; justify-content: center; gap: 18px;
  }
  .title-link .rule {
    width: 210px; height: 2px; background: var(--navy);
  }
  .title-link .word {
    font-family: "Anton", sans-serif;
    font-size: 92px; line-height: 1;
    color: var(--navy);
  }
  .title-accent {
    top: 470px; height: 175px;
    display: flex; align-items: flex-end; justify-content: center; gap: 4px;
    font-family: "Anton", sans-serif;
    font-size: 138px; line-height: 1;
    color: var(--red);
  }
  .title-accent .figure {
    width: 58px; height: 172px;
    background: linear-gradient(180deg, var(--figure-top) 0%, var(--figure-top) 40%, var(--figure-bottom) 100%);
    border-radius: 22px 22px 4px 4px;
    margin: 0 6px 6px;
  }
  .subtitle {
    top: 712px;
    font-family: "Roboto Condensed", sans-serif;
    font-weight: 300;
    font-size: 74px; line-height: 1.12;
    color: var(--navy);
  }
  .band {
    position: absolute; left: 0; bottom: 0;
    width: 100%; height: 96px;
    background: linear-gradient(90deg, var(--navy-deep) 0%, var(--navy) 50%, var(--navy-deep) 100%);
    border-top: 3px solid var(--rule-grey);
  }
  .author {
    top: 4px;
    font-family: "Roboto Condensed", sans-serif;
    font-weight: 400;
    font-size: 88px; line-height: 1;
    letter-spacing: 6px;
    color: var(--band-text);
  }
</style>
</head>
<body>
  <main class="cover">
    <h1 class="book-title">
      <span class="title-main">Lanterns</span>
      <span class="title-link">
        <span class="rule"></span>
        <span class="word">Over</span>
        <span class="rule"></span>
      </span>
      <span class="title-accent">
        <span>Harbor</span>
        <span class="figure" role="img" aria-label="Illustration of a man in cap and suspenders walking away with a cane"></span>
        <span>Gate</span>
      </span>
    </h1>
    <p class="subtitle">Notes on<br>Quiet Ambition</p>
    <footer class="band">
      <p class="author">AUTHOR NAME</p>
    </footer>
  </main>
</body>
</html>
```